Powerpoint Design for business and consulting company - Brennig-Tautz

I am searching a design specialist who can help me to create a PowerPoint Design for my company. I'm in the business coaching and consulting industry.

The PPT master should be easy to use and include professional formatting (using the fonts of my website). In general, the slide master should have the look and feel of my website (in terms of fonts, colors, logos, possibility to place big photographs, having text and graph slides as well as photo slides with just 1 key message).

The PowerPoint design should fit my cooperate Identity (please see my website https://brennig-tautz.de).
My logos are attached.

Additional information:
- wide screen format - 16: 9
- right set up of a fitting color scheme
https: // tintrow. io / f6ded1-bfcbce-807f84-9cd3d1-666666
# 666666 (Dim Gray) - body / heading text
# 807F84 (Gray Web)
#BFCBCE (Silver Sand) - link hover
# 9cd3d1 (Powder Blue) - Link color
# F6DED1 (Champagne Pink)

- creation of chart templates, using chart tools, and different chart types etc.
- creation of different slide layouts to place content, pictures (in different sizes), optionally Media
- set up of display guide lines
- as well as standard elements, such as text boxes, lines, default shapes, etc.

• Powerpoint Design needs to have:
https://tintrow.io/f6ded1-bfcbce-807f84-9cd3d1-666666
# 807F84 (Gray Web)
# F6DED1 (Champagne Pink)

```html
<!DOCTYPE html>
<html lang="en">
<head>
<meta charset="utf-8">
<title>Business Team – Brennig-Tautz</title>
<link href="https://fonts.googleapis.com/css2?family=Open+Sans:wght@300;400&family=Source+Sans+3:wght@600;700&display=swap" rel="stylesheet">
<style>
  :root {
    --ink: #333033;
    --body-text: #3f3f3f;
    --champagne: #f6ded1;
    --silver-sand: #bfcbce;
    --powder-blue: #9cd3d1;
    --gray-web: #807f84;
    --paper: #fefefe;
  }
  html, body {
    margin: 0;
    padding: 0;
    overflow: hidden;
    background: var(--paper);
  }
  .slide {
    position: relative;
    width: 1200px;
    height: 674px;
    overflow: hidden;
    background: var(--paper);
    font-family: "Open Sans", Arial, sans-serif;
    color: var(--body-text);
  }
  .slide-title {
    position: absolute;
    left: 110px;
    top: 58px;
    margin: 0;
    font-family: "Source Sans 3", Arial, sans-serif;
    font-weight: 700;
    font-size: 27px;
    letter-spacing: 0.2px;
    color: var(--ink);
  }
  .brand {
    position: absolute;
    right: 96px;
    top: 48px;
    display: flex;
    align-items: center;
    gap: 9px;
    font-family: "Open Sans", Arial, sans-serif;
    font-weight: 400;
    font-size: 19px;
    color: #1a1a1a;
  }
  .brand-mark {
    width: 14px;
    height: 14px;
    border-radius: 50%;
    background: #1a1a1a;
  }
  .team {
    position: absolute;
    top: 214px;
    left: 0;
    width: 1200px;
  }
  .member {
    position: absolute;
    top: 0;
    width: 200px;
    margin-left: -100px;
    text-align: center;
  }
  .member-photo {
    display: block;
    width: 152px;
    height: 152px;
    margin: 0 auto;
    border-radius: 50%;
  }
  .photo-john { background: radial-gradient(circle at 45% 40%, #d9b9a3 0%, #9b8276 40%, #3b3f4a 80%, #e9ebea 100%); }
  .photo-lim { background: radial-gradient(circle at 50% 42%, #d8ab92 0%, #7a5242 45%, #2a2220 80%, #b28a70 100%); }
  .photo-oliver { background: radial-gradient(circle at 50% 40%, #caa088 0%, #8f7868 42%, #a8bfdb 78%, #efe6d6 100%); }
  .region-tag {
    position: absolute;
    top: 10px;
    left: 128px;
    width: 69px;
    height: 18px;
    border-radius: 9px;
    font-size: 12px;
    line-height: 18px;
    color: var(--ink);
    text-align: center;
  }
  .tag-europe { background: var(--champagne); }
  .tag-asia { background: var(--silver-sand); }
  .tag-africa { background: var(--powder-blue); }
  .member-name {
    margin: 22px 0 0;
    font-family: "Source Sans 3", Arial, sans-serif;
    font-weight: 600;
    font-size: 18px;
    letter-spacing: -0.4px;
    color: var(--ink);
  }
  .member-role {
    margin: 6px 0 0;
    font-family: "Source Sans 3", Arial, sans-serif;
    font-weight: 600;
    font-size: 9.5px;
    line-height: 12px;
    color: #222;
  }
  .summary {
    position: absolute;
    left: 120px;
    top: 506px;
    width: 960px;
    margin: 0;
    font-weight: 300;
    font-size: 13.5px;
    line-height: 17px;
    text-align: center;
    color: #2f2f2f;
  }
  .footer-band {
    position: absolute;
    left: 0;
    top: 637px;
    width: 1200px;
    height: 37px;
  }
  .page-number {
    position: absolute;
    right: 32px;
    top: 642px;
    font-family: "Open Sans", Arial, sans-serif;
    font-size: 21px;
    color: var(--ink);
  }
</style>
</head>
<body>
<main class="slide">
  <h1 class="slide-title">BUSINESS TEAM</h1>

  <div class="brand">
    <span class="brand-mark"></span>
    <span class="brand-name">Britta Brennig-Tautz</span>
  </div>

  <section class="team">
    <article class="member" style="left:335px;">
      <div class="member-photo photo-john" role="img" aria-label="Portrait photo of Mr. John Doe"></div>
      <span class="region-tag tag-europe">Europe</span>
      <h2 class="member-name">MR. JOHN DOE</h2>
      <p class="member-role">Lorem ipsum dolar sit amet<br>voluptatem fugit aut</p>
    </article>
    <article class="member" style="left:598px;">
      <div class="member-photo photo-lim" role="img" aria-label="Portrait photo of Mrs. Lim Doe"></div>
      <span class="region-tag tag-asia">Asia</span>
      <h2 class="member-name">MRS. LIM DOE</h2>
      <p class="member-role">Lorem ipsum dolar sit amet<br>voluptatem fugit aut</p>
    </article>
    <article class="member" style="left:861px;">
      <div class="member-photo photo-oliver" role="img" aria-label="Portrait photo of Mr. Oliver Doe"></div>
      <span class="region-tag tag-africa">Africa</span>
      <h2 class="member-name">MR. OLIVER DOE</h2>
      <p class="member-role">Lorem ipsum dolar sit amet<br>voluptatem fugit aut</p>
    </article>
  </section>

  <p class="summary">Aspernatur magni quae aperiam aut veritatis beatae eos aut voluptas doloremque perspiciatis error natus natus, qui aut eaque inventore aut quasi consequuntur consequuntur ipsa aspernatur iste sit sit, quae explicabo dicta quasi sed enim accusantium laudantium aut quia architecto</p>

  <svg class="footer-band" viewBox="0 0 1200 37" width="1200" height="37" aria-hidden="true">
    <rect x="0" y="0" width="1200" height="37" fill="#f6ded1"/>
    <polygon points="1102,0 1200,0 1200,37 1088,37" fill="#9cd3d1"/>
  </svg>
  <span class="page-number">20</span>
</main>
</body>
</html>
```